Oven Cleaning Business owner needs business card design

Hi there,
Would like for a business card to be designed for myself, the owner of a professional oven cleaning business on the Sunshine Coast.
Would like it to look sleek, and modern-ish. Bit creative is encouraged too.
Include following:
Name/title: Corin ter Haghe, Owner
Phone number: 1300 482 916
Email: info@hearthshinecrew.com.au
Website: www.hearthshinecrew.com.au

```html
<!DOCTYPE html>
<html lang="en">
<head>
<meta charset="utf-8">
<title>Hearthshine Crew – Business Card</title>
<link rel="stylesheet" href="https://fonts.googleapis.com/css2?family=Arimo:ital,wght@0,400;0,700;1,400&display=swap">
<style>
  :root {
    --teal: #54c4ca;
    --teal-light: #6fd0d5;
    --ink: #1d1d1f;
    --paper: #ffffff;
    --backdrop: #2a2a2c;
  }
  * { box-sizing: border-box; margin: 0; padding: 0; }
  html, body {
    width: 1200px; height: 900px; overflow: hidden;
    background: var(--backdrop);
    font-family: "Arimo", Arial, sans-serif;
  }
  .sheet {
    width: 1200px; height: 900px;
    display: flex; flex-direction: column; align-items: center; justify-content: center;
    gap: 40px;
  }
  .card {
    width: 700px; height: 400px; position: relative; overflow: hidden;
    box-shadow: 0 10px 30px rgba(0,0,0,.45);
  }

  /* Front */
  .card--front { background: var(--paper); }
  .card--front .brand {
    position: absolute; left: 52px; top: 154px; width: 290px;
    display: flex; align-items: center; gap: 12px;
  }
  .brand__dot {
    width: 40px; height: 40px; border-radius: 50%; background: var(--teal); flex: none;
  }
  .brand__name {
    font-weight: 700; font-size: 26px; color: var(--ink); line-height: 1; white-space: nowrap;
  }
  .divider {
    position: absolute; left: 372px; top: 110px; width: 1px; height: 160px; background: var(--ink);
  }
  .contact { position: absolute; left: 398px; top: 118px; }
  .contact__name { font-weight: 700; font-size: 25px; color: var(--teal); line-height: 1.1; white-space: nowrap; }
  .contact__role { font-size: 16px; color: var(--ink); margin-top: 2px; }
  .contact__list { list-style: none; margin-top: 22px; }
  .contact__item {
    display: flex; align-items: center; gap: 9px; white-space: nowrap;
    font-size: 16px; color: var(--ink); line-height: 1; margin-bottom: 11px;
  }
  .contact__item svg { width: 15px; height: 15px; flex: none; }
  .stripe {
    position: absolute; left: 0; right: 0; bottom: 0; height: 26px; background: var(--teal);
  }
  .stripe::before {
    content: ""; position: absolute; left: 0; right: 0; top: -9px; height: 2px; background: var(--ink);
  }

  /* Back */
  .card--back { background: var(--teal); }
  .back__glow {
    position: absolute; inset: 0;
    background: radial-gradient(circle at 80% 25%, var(--teal-light) 0%, transparent 40%),
                radial-gradient(circle at 20% 80%, var(--teal-light) 0%, transparent 35%);
  }
  .card--back .brand {
    position: absolute; inset: 0;
    display: flex; align-items: center; justify-content: center; gap: 20px;
  }
  .card--back .brand__dot { width: 80px; height: 80px; background: var(--paper); }
  .card--back .brand__name { color: var(--paper); font-size: 54px; }
</style>
</head>
<body>
<main class="sheet">
  <section class="card card--front">
    <div class="brand">
      <span class="brand__dot"></span>
      <span class="brand__name">Hearthshine Crew</span>
    </div>
    <div class="divider"></div>
    <div class="contact">
      <p class="contact__name">Corin ter Haghe</p>
      <p class="contact__role">Owner</p>
      <ul class="contact__list">
        <li class="contact__item">
          <svg viewBox="0 0 24 24" fill="var(--teal)"><path d="M6.6 10.8a15.1 15.1 0 0 0 6.6 6.6l2.2-2.2a1 1 0 0 1 1-.25 11.4 11.4 0 0 0 3.6.57 1 1 0 0 1 1 1V20a1 1 0 0 1-1 1A17 17 0 0 1 3 4a1 1 0 0 1 1-1h3.5a1 1 0 0 1 1 1c0 1.25.2 2.45.57 3.6a1 1 0 0 1-.25 1z"/></svg>
          1300 482 916
        </li>
        <li class="contact__item">
          <svg viewBox="0 0 24 24" fill="var(--teal)"><path d="M2 5h20v14H2z"/><path d="M2 5l10 8 10-8" fill="none" stroke="#fff" stroke-width="1.8"/></svg>
          info@hearthshinecrew.com.au
        </li>
        <li class="contact__item">
          <svg viewBox="0 0 24 24" fill="none" stroke="var(--teal)" stroke-width="2"><circle cx="12" cy="12" r="9"/><path d="M3 12h18M12 3c3 3 3 15 0 18M12 3c-3 3-3 15 0 18"/></svg>
          www.hearthshinecrew.com.au
        </li>
      </ul>
    </div>
    <div class="stripe"></div>
  </section>

  <section class="card card--back">
    <div class="back__glow" role="img" aria-label="Soft sparkle pattern in light teal"></div>
    <div class="brand">
      <span class="brand__dot"></span>
      <span class="brand__name">Hearthshine Crew</span>
    </div>
  </section>
</main>
</body>
</html>
```